Business card for Harbor Crafters
Looking for creativity
Professional
Dominic Farrow
Owner Operator
47 S Pell Avenue
Brookvale, NH 19842
@domfarrow
craftharborco@mailvane.com
www.craftharborco.com
Looking for a creative business card for my company. I have a logo and like the feel of it. The business card should have a contemporary feel and be interesting.
The name of the company and the website

```html
<!DOCTYPE html>
<html lang="en">
<head>
<meta charset="utf-8">
<title>Harbor Crafters — Business Card</title>
<link rel="stylesheet" href="https://fonts.googleapis.com/css2?family=Noto+Serif:wght@400;700&display=swap">
<style>
  :root {
    --page-bg: #ecebe8;
    --card-bg: #ffffff;
    --brand-blue: #1f5ea8;
    --brand-blue-dark: #17498a;
    --swoosh-grey: #b9bcc1;
    --text-dark: #333638;
    --text-muted: #66696c;
    --divider: #d9dadc;
  }
  * { box-sizing: border-box; margin: 0; padding: 0; }
  html, body {
    width: 1200px; height: 780px; overflow: hidden;
    background: var(--page-bg);
    font-family: "Noto Serif", Georgia, serif;
  }
  .card {
    position: absolute; left: 80px; top: 93px;
    width: 1040px; height: 594px;
    background: var(--card-bg);
    border-radius: 36px;
    overflow: hidden;
    box-shadow: 0 10px 30px rgba(0,0,0,0.15);
  }
  .card__bands { position: absolute; inset: 0; width: 100%; height: 100%; }
  .brand {
    position: absolute; left: 30px; top: 244px; width: 420px;
    display: flex; align-items: center; justify-content: center; gap: 12px;
  }
  .brand__mark { width: 20px; height: 20px; background: var(--brand-blue); flex: none; }
  .brand__name {
    color: var(--brand-blue); font-weight: 700; font-size: 36px;
    letter-spacing: 1px; white-space: nowrap;
  }
  .divider {
    position: absolute; left: 480px; top: 40px; width: 2px; height: 380px;
    background: linear-gradient(to bottom, transparent, var(--divider) 15%, var(--divider) 85%, transparent);
    box-shadow: 3px 0 6px rgba(0,0,0,0.06);
  }
  .details { position: absolute; left: 520px; top: 58px; color: var(--text-dark); }
  .details__name { color: var(--brand-blue); font-weight: 700; font-size: 34px; line-height: 1.2; }
  .details__title { color: var(--text-muted); font-size: 21px; margin-top: 2px; }
  .details__address { font-size: 21px; line-height: 1.5; margin-top: 46px; }
  .contact-list { list-style: none; margin-top: 34px; font-size: 21px; }
  .contact-list li { display: flex; align-items: center; gap: 14px; height: 32px; }
  .contact-list svg { width: 20px; height: 20px; flex: none; }
</style>
</head>
<body>
  <div class="card">
    <svg class="card__bands" viewBox="0 0 1040 594" preserveAspectRatio="none" aria-hidden="true">
      <defs>
        <linearGradient id="greyFade" x1="0" x2="1">
          <stop offset="0" stop-color="#d4d6d9"/>
          <stop offset="1" stop-color="#9fa3a8"/>
        </linearGradient>
        <linearGradient id="blueBand" x1="0" y1="0" x2="0" y2="1">
          <stop offset="0" stop-color="#2a6cb8"/>
          <stop offset="1" stop-color="#17498a"/>
        </linearGradient>
      </defs>
      <path d="M0 452 C 320 462, 720 452, 1040 380 L1040 398 C 720 470, 320 478, 0 470 Z" fill="url(#greyFade)"/>
      <path d="M0 478 C 320 486, 720 478, 1040 405 L1040 594 L0 594 Z" fill="url(#blueBand)"/>
    </svg>

    <div class="brand">
      <span class="brand__mark"></span>
      <span class="brand__name">HARBOR CRAFTERS</span>
    </div>

    <div class="divider"></div>

    <div class="details">
      <h1 class="details__name">Dominic Farrow</h1>
      <p class="details__title">Owner Operator</p>
      <p class="details__address">47 S Pell Avenue<br>Brookvale, NH 19842</p>
      <ul class="contact-list">
        <li>
          <svg viewBox="0 0 20 20"><path d="M5 2 L8 2 L9 6 L7 8 C8 11 9 12 12 13 L14 11 L18 12 L18 15 C18 17 16 18 14 18 C8 17 3 12 2 6 C2 4 3 2 5 2 Z" fill="var(--brand-blue)"/></svg>
          <span>302.555.0148</span>
        </li>
        <li>
          <svg viewBox="0 0 20 20"><circle cx="10" cy="10" r="8" fill="var(--brand-blue)"/></svg>
          <span>@domfarrow</span>
        </li>
        <li>
          <svg viewBox="0 0 20 20"><rect x="2" y="4" width="16" height="12" rx="1" fill="var(--brand-blue)"/><path d="M2.5 5 L10 11 L17.5 5" fill="none" stroke="#fff" stroke-width="1.5"/></svg>
          <span>craftharborco@mailvane.com</span>
        </li>
        <li>
          <svg viewBox="0 0 20 20"><circle cx="10" cy="10" r="8" fill="none" stroke="var(--brand-blue)" stroke-width="1.6"/><ellipse cx="10" cy="10" rx="3.5" ry="8" fill="none" stroke="var(--brand-blue)" stroke-width="1.2"/><line x1="2" y1="10" x2="18" y2="10" stroke="var(--brand-blue)" stroke-width="1.2"/></svg>
          <span>www.craftharborco.com</span>
        </li>
      </ul>
    </div>
  </div>
</body>
</html>
```